Gif Graphic for hero image on a website home page

Im looking for an gif graphic that will go in the hero section at the top of our website. You can see an example of what we are trying to accomplish here quillmark.example.

Vastelo - We are an interactive game software for business to provide employee perks. I would like this graphic to show an outline of our event pages so the viewer can see where things go like the banner, items, etc.

We run two type of events, Auctions and Raffles. Auction allow people to place bids on items, and raffles allow people to submit tickets to enter for their change to win the item. For Raffles, we have a Live interactive wheel with everyones name on it that entered to win that item. The winners are drawn through our site in a live setting and confetti is thrown around when the wheel stops on someones name.

The goal of this graphic would be to show how easy the page it to create, how easy it is to bid, how easy it is to submit a ticket to enter the raffle and then the drawling of a winner for a raffle.

some steps that can be taken our:
Step 1) Show the Banner being placed on the page and Event Name Added.
Step 2) Add two items, a Raffle Item and an Auction Item.
Step 3) Show the process to enter a bid and then submit a raffle ticket.
Step 4) Show "Drawing In Process" with the wheel popping over the page spinning and stopping on a winner. Then display some confetti with the winners name.

I don't want to use any screen shots, just recreate the page layout from the sample layout uploaded below.

I've uploaded some examples and our logo and color theme.

```html
<!DOCTYPE html>
<html lang="en">
<head>
<meta charset="utf-8">
<title>Vastelo – Event Page Layout</title>
<link href="https://fonts.googleapis.com/css2?family=Montserrat:wght@400;500;700;800&display=swap" rel="stylesheet">
<style>
  :root {
    --panel: #f4f4f4;
    --grey: #a8a8a8;
    --grey-light: #b8b8b8;
    --tile: #dedede;
    --placeholder: #e0e0e0;
    --orange: #ff6600;
    --green: #449a00;
    --ink: #3d3d3d;
    --black: #000000;
    --white: #ffffff;
  }
  * { box-sizing: border-box; margin: 0; padding: 0; }
  html, body { width: 998px; height: 1200px; overflow: hidden; background: var(--white); }
  body { position: relative; font-family: "Montserrat", sans-serif; color: var(--ink); }

  /* Sidebar with brand and builder actions; the last two slots are intentional empty placeholders */
  .sidebar { position: absolute; left: 0; top: 0; width: 249px; height: 709px; background: var(--panel); }
  .brand {
    position: absolute; left: 0; top: 30px; width: 249px; text-align: center;
    font-weight: 800; font-size: 40px; line-height: 50px; color: var(--black);
  }
  .nav-button {
    position: absolute; left: 21px; width: 206px; height: 55px; border-radius: 10px;
    background: var(--grey); color: var(--white);
    font-weight: 800; font-size: 22px; display: flex; align-items: center; justify-content: center;
  }
  .nav-button--empty { background: var(--grey-light); }
  .nav-button--empty span { display: block; width: 141px; height: 21px; background: var(--placeholder); }

  /* Banner slot, shown as an empty block where the event banner is placed */
  .banner { position: absolute; left: 249px; top: 0; width: 749px; height: 110px; background: var(--grey); }

  .event-panel { position: absolute; left: 281px; top: 116px; width: 685px; height: 570px; background: var(--panel); }
  .event-title { position: absolute; left: 25px; top: 22px; font-weight: 800; font-size: 22px; line-height: 26px; color: var(--ink); }
  .event-host { position: absolute; left: 25px; top: 48px; font-weight: 500; font-size: 22px; line-height: 26px; color: var(--ink); }
  .event-host em { font-style: normal; color: var(--orange); }

  .item-card { position: absolute; top: 124px; width: 266px; height: 378px; background: var(--tile); }
  .item-card--auction { left: 38px; }
  .item-card--raffle { left: 343px; }
  .item-media { position: relative; height: 201px; }
  .item-card--auction .item-media { background: var(--grey); color: var(--grey); }
  .item-card--raffle .item-media { background: var(--orange); color: var(--orange); }
  .item-media svg { position: absolute; left: 47px; top: 27px; width: 168px; height: 147px; }

  .status-tick { position: absolute; left: 102px; top: 227px; width: 62px; height: 62px; }
  .item-action {
    position: absolute; left: 29px; top: 313px; width: 205px; height: 55px; border-radius: 10px;
    color: var(--white); font-weight: 800; font-size: 22px;
    display: flex; align-items: center; justify-content: center;
  }
  .item-action--bid { background: var(--green); }
  .item-action--ticket { background: var(--grey); }

  .preview-note { position: absolute; left: 161px; top: 906px; font-size: 22px; line-height: 28px; font-weight: 500; color: var(--ink); white-space: nowrap; }
  .preview-note strong { font-weight: 800; margin-left: 8px; }
</style>
</head>
<body>
  <aside class="sidebar">
    <div class="brand">Vastelo</div>
    <div class="nav-button" style="top:155px">Add Event</div>
    <div class="nav-button" style="top:243px">Add Raffle</div>
    <div class="nav-button" style="top:330px">Add Auction</div>
    <div class="nav-button nav-button--empty" style="top:417px"><span></span></div>
    <div class="nav-button nav-button--empty" style="top:505px"><span></span></div>
  </aside>

  <header class="banner"></header>

  <main class="event-panel">
    <h1 class="event-title">Event Name</h1>
    <p class="event-host">By <em>Rowan</em></p>

    <section class="item-card item-card--auction">
      <div class="item-media">
        <svg viewBox="0 0 243 212" aria-hidden="true">
          <rect width="243" height="212" rx="32" fill="#ffffff"/>
          <circle cx="69" cy="68" r="23" fill="currentColor"/>
          <path d="M15 168 L62 129 L106 157 L166 97 L228 129 L228 184 Q228 197 215 197 L30 197 Q15 197 15 184 Z" fill="currentColor"/>
        </svg>
      </div>
      <svg class="status-tick" viewBox="0 0 62 62" aria-hidden="true">
        <circle cx="31" cy="31" r="31" fill="#449a00"/>
        <path d="M19 32 L28 41 L44 22" fill="none" stroke="#dedede" stroke-width="6" stroke-linecap="round" stroke-linejoin="round"/>
      </svg>
      <div class="item-action item-action--bid">Bid</div>
    </section>

    <section class="item-card item-card--raffle">
      <div class="item-media">
        <svg viewBox="0 0 243 212" aria-hidden="true">
          <rect width="243" height="212" rx="32" fill="#ffffff"/>
          <circle cx="69" cy="68" r="23" fill="currentColor"/>
          <path d="M15 168 L62 129 L106 157 L166 97 L228 129 L228 184 Q228 197 215 197 L30 197 Q15 197 15 184 Z" fill="currentColor"/>
        </svg>
      </div>
      <div class="item-action item-action--ticket">Submit Ticket</div>
    </section>
  </main>

  <p class="preview-note">TO Preview the gif go to:<strong>https://vastelo-preview.example</strong></p>
</body>
</html>
```